Harvest Bridge Christian Ministry needs a Conference Ad

We are a Christian nonprofit focused on eliminating systemic poverty and helping believers function as ministers in their workplaces. The 2025 Lantern Path Global Conference coming up in October, and we need an ad for social media (facebook, instagram, and X) and our website in order to get people excited to attend! We are looking for a modern and sleek design that incorporates our logo (attached file). You can either put just the butterfly and then write our company name separately somewhere in the design or use it as is (we used Gotham font for the logo). We want to emphasize the joy of in-person connection at the conference, so you could possibly include stock photos of young people gathering together. You could also include the attached photo of our founders in the design and say “with Mel and Dora Quintavan". Also, include the conference dates, which are October 9-12, 2025, and say “come in person or join online”. Lastly, please include the tagline “from the Pellmore Awakening to Worldwide Transformation”. NOTE: I’m attaching AN EXAMPLE I’ve created of how the design could look, which you can feel free to use for inspiration.
Young people on Instagram and facebook
- Gotham

```html
<!DOCTYPE html>
<html lang="en">
<head>
<meta charset="utf-8">
<title>Lantern Path Global Conference – Harvest Bridge</title>
<link rel="stylesheet" href="https://fonts.googleapis.com/css2?family=Montserrat:ital,wght@0,300;0,600;0,700;0,800;1,800&display=swap">
<style>
  :root {
    --stage: #1c1c1a;
    --navy-top: #0e3f60;
    --navy-mid: #135f85;
    --teal-glow: #1a7ea6;
    --teal-low: #2c7f9d;
    --orange: #f0913a;
    --band-top: #eea66a;
    --band-bottom: #c9763d;
    --pill-top: #e89a5c;
    --pill-bottom: #c76f33;
    --white: #ffffff;
    --photo-dark: #1d2228;
    --photo-warm: #8a6a58;
  }
  * { margin: 0; padding: 0; box-sizing: border-box; }
  html, body {
    width: 1200px; height: 1111px; overflow: hidden;
    background: var(--stage);
    font-family: "Montserrat", sans-serif;
  }
  .ad {
    position: absolute; left: 132px; top: 91px;
    width: 927px; height: 927px; overflow: hidden;
    background:
      radial-gradient(ellipse 70% 55% at 45% 85%, var(--teal-low) 0%, transparent 70%),
      radial-gradient(ellipse 80% 60% at 50% 55%, var(--teal-glow) 0%, transparent 75%),
      linear-gradient(180deg, var(--navy-top) 0%, var(--navy-mid) 45%, var(--teal-glow) 100%);
    box-shadow: 0 6px 18px rgba(0,0,0,.55);
    color: var(--white);
  }
  .brand {
    position: absolute; left: 190px; top: 49px; height: 118px;
    display: flex; align-items: center; gap: 22px;
  }
  .brand-dot { width: 62px; height: 62px; border-radius: 50%; background: var(--white); }
  .brand-name {
    font-weight: 700; font-size: 44px; letter-spacing: 2px; line-height: 1;
    color: var(--white); text-transform: uppercase;
  }
  .tagline {
    position: absolute; left: 86px; top: 237px;
    font-size: 47px; line-height: 52.5px; text-transform: uppercase;
    font-weight: 300;
  }
  .tagline-lead { font-weight: 300; display: block; }
  .tagline-focus { font-weight: 800; color: var(--orange); display: block; letter-spacing: -.5px; }
  .join-pill {
    position: absolute; left: 86px; top: 482px; width: 258px; height: 47px;
    border-radius: 24px;
    background: linear-gradient(180deg, var(--pill-top), var(--pill-bottom));
    border: 2px solid #f4c08f;
    box-shadow: 0 3px 6px rgba(0,0,0,.35);
    display: flex; align-items: center; justify-content: center;
    font-weight: 800; font-style: italic; font-size: 29px; letter-spacing: .5px;
    text-shadow: 1px 2px 2px rgba(0,0,0,.35);
  }
  .dates {
    position: absolute; left: 88px; top: 560px;
    display: flex; align-items: stretch; gap: 20px;
  }
  .dates-days { display: flex; flex-direction: column; align-items: center; }
  .dates-range { font-weight: 700; font-size: 68px; line-height: 58px; letter-spacing: -1px; }
  .dates-month { font-weight: 700; font-size: 27px; line-height: 30px; margin-top: 6px; }
  .dates-rule { width: 4px; background: var(--orange); margin-top: 2px; }
  .dates-year { font-weight: 700; font-size: 52px; line-height: 46px; letter-spacing: 1px; }
  .attend-note {
    position: absolute; left: 88px; top: 692px;
    font-weight: 600; font-size: 21px; line-height: 27px; letter-spacing: 1px;
    text-transform: uppercase;
  }
  .founders-photo {
    position: absolute; left: 439px; top: 423px; width: 488px; height: 416px;
    background:
      radial-gradient(ellipse 30% 35% at 35% 45%, var(--photo-warm) 0%, transparent 70%),
      radial-gradient(ellipse 30% 35% at 70% 30%, var(--photo-warm) 0%, transparent 70%),
      linear-gradient(180deg, rgba(29,34,40,0) 0%, var(--photo-dark) 55%);
    border-radius: 200px 200px 0 0;
  }
  .host-band {
    position: absolute; left: 0; bottom: 0; width: 100%; height: 88px;
    background: linear-gradient(180deg, var(--band-top), var(--band-bottom));
    display: flex; align-items: center; justify-content: center;
    font-weight: 600; font-size: 25px; letter-spacing: 1.5px; text-transform: uppercase;
  }
</style>
</head>
<body>
  <main class="ad">
    <div class="brand">
      <span class="brand-dot"></span>
      <span class="brand-name">Harvest Bridge</span>
    </div>

    <h1 class="tagline">
      <span class="tagline-lead">From the</span>
      <span class="tagline-lead">Pellmore Awakening to</span>
      <span class="tagline-focus">Worldwide</span>
      <span class="tagline-focus">Transformation</span>
    </h1>

    <div class="founders-photo" role="img" aria-label="Photo of founders Mel and Dora Quintavan together"></div>

    <div class="join-pill">JOIN ONLINE</div>

    <div class="dates">
      <div class="dates-days">
        <span class="dates-range">9-12</span>
        <span class="dates-month">OCTOBER</span>
      </div>
      <span class="dates-rule"></span>
      <div class="dates-year">20<br>25</div>
    </div>

    <p class="attend-note">Come in person<br>or join online</p>

    <div class="host-band">With Mel and Dora Quintavan</div>
  </main>
</body>
</html>
```